Business Card Design Project - IT Company

CLOUD IT company working with medium to large corporate clients requires 2 sided Business Card design.

Strong, Professional and modern is what I am looking for.

The Logo JPG attached has all the colour palette options. which consist of Red and Silver on various backgrounds

Preferred option for the Back of card is either Silver Text on Red or Silver Text on Black. Though this is not concrete. Surprise me.

Logo must be prominent along with Contact details of the staff member

Tagline can be all Capitals " CLOUD MANAGED SERVICES"

I will look to provide feedback and tweaks to get the right design so it should be a fun process.

I will provide the layered files to the top few contenders.

Reason: Leaving the door open for some creativity. Don't forget this is an technology company. .

Target Market(s)

Leaders, decision makers, CEOs, CIOs,

Industry/Entity Type

Business

Requirements
Must have
• Data must have is

Company Name: Velquora
Tagline: Cloud Managed Services

No Particular order

First Name Last name
Director
Mobile 0452 987 654
www.velquora.com
First.Lastname@velquora.com
Suite 5, 48 Marlowe Lane, Sydney NSW 2000

```html
<!DOCTYPE html>
<html lang="en">
<head>
<meta charset="utf-8">
<title>Velquora Business Card</title>
<link rel="stylesheet" href="https://fonts.googleapis.com/css2?family=Arimo:wght@400;700&display=swap">
<style>
  :root {
    --bg: #ececec;
    --card-white: #f4f4f4;
    --brand-red: #981a20;
    --ink: #222222;
    --ink-soft: #555555;
    --silver: #d6d6d6;
    --rule: #9a9a9a;
  }
  * { box-sizing: border-box; margin: 0; padding: 0; }
  html, body { width: 1200px; height: 800px; overflow: hidden; }
  body {
    background: var(--bg);
    font-family: "Arimo", Arial, sans-serif;
    color: var(--ink);
    position: relative;
  }
  .card {
    position: absolute;
    top: 245px;
    width: 530px;
    height: 303px;
    box-shadow: 0 6px 18px rgba(0,0,0,0.12);
  }
  .card-front { left: 50px; background: var(--card-white); }
  .card-back { left: 620px; background: var(--brand-red); }

  .wordmark {
    position: absolute;
    display: flex;
    align-items: center;
    gap: 12px;
  }
  .wordmark-dot {
    width: 26px; height: 26px;
    border-radius: 50%;
    background: var(--brand-red);
    flex: none;
  }
  .wordmark-name {
    font-weight: 700;
    font-size: 40px;
    line-height: 1;
    letter-spacing: -0.5px;
    color: var(--ink);
  }
  .wordmark-tagline {
    display: block;
    font-size: 10.5px;
    font-weight: 400;
    letter-spacing: 0.6px;
    margin-top: 4px;
    color: var(--ink);
  }
  .card-front .wordmark { left: 44px; top: 52px; }

  .contact {
    position: absolute;
    right: 28px;
    top: 42px;
    text-align: right;
    font-size: 11.5px;
    line-height: 15px;
  }
  .contact-address { margin-bottom: 8px; }
  .contact-line { display: flex; justify-content: flex-end; align-items: center; gap: 8px; }
  .contact-icon {
    width: 11px; height: 11px;
    background: var(--brand-red);
    border-radius: 2px;
    flex: none;
  }
  .contact-icon.blank { background: transparent; }

  .divider {
    position: absolute;
    left: 252px;
    top: 178px;
    width: 48px;
    height: 1px;
    background: var(--rule);
    transform: rotate(25deg);
    transform-origin: left center;
  }

  .person {
    position: absolute;
    left: 36px;
    bottom: 30px;
    display: flex;
    align-items: flex-start;
    gap: 10px;
  }
  .person-marker { width: 12px; height: 14px; margin-top: 12px; }
  .person-name { font-weight: 700; font-size: 15px; }
  .person-role { font-size: 12px; color: var(--brand-red); }

  .card-back .wordmark { right: 40px; bottom: 58px; }
  .card-back .wordmark-name { color: var(--silver); font-size: 46px; }
  .card-back .wordmark-dot { background: var(--silver); }
  .card-back .wordmark-tagline { color: var(--silver); text-align: right; }
</style>
</head>
<body>
  <section class="card card-front" aria-label="Card front">
    <div class="wordmark">
      <span class="wordmark-dot"></span>
      <div>
        <span class="wordmark-name">Velquora</span>
        <span class="wordmark-tagline">CLOUD MANAGED SERVICES</span>
      </div>
    </div>

    <div class="contact">
      <div class="contact-address">
        <div class="contact-line">Suite 5, 48 Marlowe Lane <span class="contact-icon blank"></span></div>
        <div class="contact-line">Sydney NSW 2000 <span class="contact-icon"></span></div>
      </div>
      <div class="contact-line">0452 987 654 <span class="contact-icon"></span></div>
      <div class="contact-line">First.Lastname@velquora.com <span class="contact-icon"></span></div>
      <div class="contact-line">www.velquora.com <span class="contact-icon blank"></span></div>
    </div>

    <div class="divider"></div>

    <div class="person">
      <svg class="person-marker" viewBox="0 0 12 14" aria-hidden="true"><polygon points="0,0 12,7 0,14" fill="#222222"/></svg>
      <div>
        <div class="person-name">Daniel Marsh</div>
        <div class="person-role">President</div>
      </div>
    </div>
  </section>

  <section class="card card-back" aria-label="Card back">
    <div class="wordmark">
      <span class="wordmark-dot"></span>
      <div>
        <span class="wordmark-name">Velquora</span>
        <span class="wordmark-tagline">CLOUD MANAGED SERVICES</span>
      </div>
    </div>
  </section>
</body>
</html>
```